Minimalist- A clean spacious and crisp design for a Security Consulting Company

I need a design for a security consultant that deals with the upper end of town for security design, including CCTV and other electronic design. I need it to look spacious and be very simplistic in design. I want to keep it looking like Plonka or VANTU's website. I have experience in business intelligence. and have a lot of high end clients in the diamond industry and mining. My key area of income is consulting and taking them from normal to excellent security.
Target Market(s)
People interested in doing business with me
Industry/Entity Type
Electronic
Coding
Coded - Design and coding required
Number of Pages Required
4 page
Requirements
Must have
- The least amount of text possible
- A simple and nice front page with the logo.
- A contact us button
- Specialised projects button
- About us button
- Business intelligence button
Should not have
- Cluttered un-useful information

```html
<!DOCTYPE html>
<html lang="en">
<head>
<meta charset="utf-8">
<title>Kestrel Ward — Security Design</title>
<link href="https://fonts.googleapis.com/css2?family=Arimo:wght@400;700&display=swap" rel="stylesheet">
<style>
:root{
  --red:#c8252a;
  --red-dark:#a81c21;
  --ink:#1f1f1f;
  --text:#4a4a4a;
  --nav:#3b3c3f;
  --nav-line:#2c2d2f;
  --footer:#2a2a2b;
  --white:#ffffff;
}
*{box-sizing:border-box;margin:0;padding:0}
html,body{width:754px;height:1200px;overflow:hidden;background:var(--white)}
body{position:relative;font-family:"Arimo",Arial,sans-serif;color:var(--text)}
.abs{position:absolute}
.top-rule{left:46px;top:0;width:661px;height:4px;background:var(--red-dark)}
.brand{left:46px;top:26px;display:flex;align-items:center;gap:8px}
.brand-mark{width:22px;height:22px;background:var(--red)}
.brand-name{font-size:20px;font-weight:700;color:var(--ink);letter-spacing:-.3px}
.main-nav{left:46px;top:76px;width:661px;height:38px;background:var(--nav);display:flex}
.main-nav a{display:flex;align-items:center;justify-content:center;color:var(--white);font-size:10px;text-decoration:none;border-right:1px solid var(--nav-line)}
.main-nav a:last-child{border-right:0}
.main-nav a.active{background:var(--red)}
.hero{left:0;top:114px;width:754px;height:358px;background:radial-gradient(ellipse at 30% 40%,#8a8a8c 0%,#5c5c5e 45%,#3e3e40 100%)}
.hero-title{right:47px;top:128px;width:380px;text-align:right;color:var(--white);font-size:20.5px;line-height:31px;letter-spacing:.4px}
.hero-title .big{font-size:28px}
.hero-dots{right:48px;top:236px;display:flex;gap:3px}
.hero-dots span{width:6px;height:6px;border-radius:50%;background:#1e1e1e}
.hero-dots span.on{background:var(--red)}
.section-title{left:0;width:754px;text-align:center;font-size:22px;font-weight:700;color:var(--ink)}
.section-title em{font-style:normal;color:var(--red)}
.about-title{top:510px}
.about-copy{left:54px;top:551px;width:643px;text-align:justify;text-align-last:center;font-size:8.6px;line-height:16.2px;letter-spacing:.15px}
.btn{display:flex;align-items:center;justify-content:center;background:var(--red);color:var(--white);font-size:9.5px;text-decoration:none}
.about-btn{left:334px;top:625px;width:86px;height:25px}
.services{left:0;top:670px;width:754px;height:274px;background:linear-gradient(90deg,#3d3d3f 0%,#5a5a5c 45%,#3a3a3c 75%,#2c2c2e 100%)}
.services-title{top:700px;color:var(--white)}
.service{top:750px;width:196px;text-align:center;color:var(--white)}
.service .icon{width:56px;height:56px;margin:0 auto;border-radius:50%;background:var(--red);display:flex;align-items:center;justify-content:center;box-shadow:0 0 0 2px rgba(200,37,42,.35)}
.service h3{margin-top:16px;font-size:12.5px;font-weight:400;letter-spacing:.4px}
.service p{margin-top:9px;font-size:7.6px;line-height:14px;text-align:justify;text-align-last:center;color:#e2e2e2;letter-spacing:.2px}
.service .btn{width:56px;height:18px;margin:8px auto 0;font-size:9px}
.projects-title{top:981px}
.carousel-arrows{left:679px;top:991px;display:flex;gap:6px}
.thumb{top:1020px;width:152px;height:87px}
.site-footer{left:0;top:1142px;width:754px;height:58px;background:var(--footer)}
.copyright{left:48px;top:1171px;font-size:8px;color:#d8d8d8}
.social{left:606px;top:1165px;display:flex;gap:3px}
.social span{width:18px;height:18px;border-radius:50%;background:var(--white)}
</style>
</head>
<body>
<div class="abs top-rule"></div>

<header class="abs brand">
  <span class="brand-mark"></span>
  <span class="brand-name">Kestrel Ward</span>
</header>

<nav class="abs main-nav">
  <a class="active" href="#" style="width:87px">Home</a>
  <a href="#" style="width:126px">About us</a>
  <a href="#" style="width:166px">Specialised Projects</a>
  <a href="#" style="width:168px">Business Intelligence</a>
  <a href="#" style="width:114px">Contact us</a>
</nav>

<section class="abs hero" role="img" aria-label="Close-up photograph of a wall-mounted CCTV security camera"></section>
<h1 class="abs hero-title" style="font-weight:400">A company which provides security design, including <span class="big">CCTV</span> and other electronic design</h1>
<div class="abs hero-dots"><span class="on"></span><span></span><span></span><span></span></div>

<h2 class="abs section-title about-title">About <em>Us</em></h2>
<p class="abs about-copy">Dolor nunc vule putateulr ips dol consec.Donec semp ertet lacinia ultri cie upien disse comete dolo lectus fgilla itollicil tua ludin dolor nec met quam accumsan dolore condime netus lullam utlacus adipiscing ipsum molestie euismod estibulum vel libero ipsum sit amet. Dolor nunc vule putateulr ips dol consec.Donec semp ertet lacinia ultri cie upien disse comete dolo lectus fgilla itollicil tua ludin dolor nec met quam accumsan dolore condime netus lullam utlacus adipiscing ipsum molestie euismod estibulum vel libero ipsum sit amet.</p>
<a class="abs btn about-btn" href="#">Read More</a>

<section class="abs services" role="img" aria-label="Dim photograph of a glass office interior with a businessman"></section>
<h2 class="abs section-title services-title" style="color:var(--white)">Featured Services</h2>

<div class="abs service" style="left:52px">
  <div class="icon"><svg width="20" height="22" viewBox="0 0 20 22"><path d="M2 2h16v8c0 6-4 9-8 11-4-2-8-5-8-11z" fill="#fff"/><path d="M10 5v12c-2-1-4-3-4-7V5z" fill="var(--red)"/></svg></div>
  <h3>ESTIBULUM VEL</h3>
  <p>Sed ut perspiciatis unde omnis iste natus error sit voluptatem accusantium doloremque laudantium, totam rem aperiam, eaque ipsa.</p>
  <a class="btn" href="#">More</a>
</div>
<div class="abs service" style="left:281px">
  <div class="icon"><svg width="20" height="22" viewBox="0 0 20 22"><circle cx="10" cy="6" r="5" fill="#fff"/><path d="M1 21c0-6 4-9 9-9s9 3 9 9z" fill="#fff"/></svg></div>
  <h3>ESTIBULUM VEL</h3>
  <p>Sed ut perspiciatis unde omnis iste natus error sit voluptatem accusantium doloremque laudantium, totam rem aperiam, eaque ipsa.</p>
  <a class="btn" href="#">More</a>
</div>
<div class="abs service" style="left:510px">
  <div class="icon"><svg width="18" height="22" viewBox="0 0 18 22"><path d="M4 10V6a5 5 0 0 1 10 0" fill="none" stroke="#fff" stroke-width="2.6" transform="translate(-3 0)"/><rect x="1" y="10" width="16" height="11" rx="1" fill="#fff"/><rect x="8" y="13" width="2" height="5" fill="var(--red)"/></svg></div>
  <h3>ESTIBULUM VEL</h3>
  <p>Sed ut perspiciatis unde omnis iste natus error sit voluptatem accusantium doloremque laudantium, totam rem aperiam, eaque ipsa.</p>
  <a class="btn" href="#">More</a>
</div>

<h2 class="abs section-title projects-title">Specialized <em>Projects</em></h2>
<div class="abs carousel-arrows">
  <svg width="12" height="10" viewBox="0 0 12 10"><path d="M11 5H2M5 1 1 5l4 4" fill="none" stroke="#222" stroke-width="1.6"/></svg>
  <svg width="12" height="10" viewBox="0 0 12 10"><path d="M1 5h9M7 1l4 4-4 4" fill="none" stroke="#aaa" stroke-width="1.6"/></svg>
</div>
<div class="abs thumb" style="left:46px;background:linear-gradient(180deg,#e4e6e8,#b9ab8c)" role="img" aria-label="Security control room desk with monitors"></div>
<div class="abs thumb" style="left:217px;background:linear-gradient(180deg,#bcd7ea 0%,#8fa860 55%,#3d4a2a 100%)" role="img" aria-label="Security guard with radio in a field"></div>
<div class="abs thumb" style="left:386px;background:linear-gradient(135deg,#5a5f6a,#2a2d35)" role="img" aria-label="Hand using a handheld metal detector"></div>
<div class="abs thumb" style="left:556px;background:linear-gradient(135deg,#3a5f90 0%,#d9dde2 60%,#4aa0d8 100%)" role="img" aria-label="Operator watching a wall of surveillance screens"></div>

<footer class="abs site-footer"></footer>
<p class="abs copyright">Copyright © 2015, Kestrelward, All Right Reserved.</p>
<div class="abs social"><span></span><span></span><span></span><span></span><span></span></div>
</body>
</html>
```